Need Business Card for our Indian Grocery Store

Industry/Entity Type

Grocery Store

Contact Information for Business Card

Manoj Varkey
Director

Store Locations:

Thomastown
482 Fenwick Road
P: 03 9581 2046

Reservoir
613 Larchmont
P: 03 9572 8814

email: pvtstores@mailbrook.net

Requirements
Must have
• Our logo Colours

```html
<!DOCTYPE html>
<html lang="en">
<head>
<meta charset="utf-8">
<title>Kesar Groceries &amp; Spices — Business Card</title>
<link rel="stylesheet" href="https://fonts.googleapis.com/css2?family=Mulish:wght@300;800&display=swap">
<style>
  :root {
    --brand-red: #e31e24;
    --ink: #1a1a1a;
    --paper: #ffffff;
    --pattern-light: #f6d2d3;
  }
  * { margin: 0; padding: 0; box-sizing: border-box; }
  html, body {
    width: 1200px;
    height: 684px;
    overflow: hidden;
    background: var(--paper);
  }
  .card {
    position: relative;
    width: 1200px;
    height: 684px;
    background: var(--paper);
    font-family: "Mulish", sans-serif;
  }
  .brand {
    position: absolute;
    top: 100px;
    left: 0;
    width: 100%;
    text-align: center;
    color: var(--brand-red);
    font-weight: 800;
    font-size: 46px;
    line-height: 1.25;
    letter-spacing: 1px;
  }
  .brand-name span { display: block; }
  .person {
    position: absolute;
    top: 402px;
    left: 0;
    width: 100%;
    text-align: center;
  }
  .person-name {
    font-weight: 800;
    font-size: 42px;
    line-height: 1.2;
    color: var(--brand-red);
  }
  .person-title {
    font-weight: 300;
    font-size: 40px;
    line-height: 1.2;
    color: var(--ink);
  }
  .border-pattern {
    position: absolute;
    left: 0;
    bottom: 0;
    width: 100%;
    height: 104px;
    background: linear-gradient(to bottom, var(--pattern-light) 0%, var(--pattern-light) 50%, var(--brand-red) 58%, var(--brand-red) 100%);
  }
</style>
</head>
<body>
  <main class="card">
    <header class="brand">
      <p class="brand-name"><span>Kesar</span><span>Groceries &amp; Spices</span></p>
    </header>

    <section class="person">
      <h1 class="person-name">Manoj Varkey</h1>
      <p class="person-title">Director</p>
    </section>

    <div class="border-pattern" role="img" aria-label="Red and white Indian paisley border pattern with stars and scalloped motifs"></div>
  </main>
</body>
</html>
```